Most Holy Awesome Pastor Neil

Harbor Point Church is an up and coming church in Wichita Falls Texas. Very contemporary. Would like a card that leaves an impression with visitors.

Industry/Entity Type

Church

Contact Information for Business Card

Pastor Neil A. Gardner940-723-7533 phone940-767-0325 faxwww.harborptfell.compastor@harborptfell.example

Colors
9bcb3c

Requirements
Should not have
• pictures

```html
<!DOCTYPE html>
<html lang="en">
<head>
<meta charset="utf-8">
<title>Harbor Point Church – Pastor Neil R. Whitcombe Business Card</title>
<link rel="stylesheet" href="https://fonts.googleapis.com/css2?family=Abel&display=swap">
<style>
  :root {
    --lime: #9cff06;
    --ink: #454b4f;
    --paper: #ffffff;
    --backdrop: #e6ebeb;
  }
  * { margin: 0; padding: 0; box-sizing: border-box; }
  html, body {
    width: 1008px;
    height: 1200px;
    overflow: hidden;
    background: var(--backdrop);
    font-family: "Abel", "Arial Narrow", sans-serif;
  }
  .canvas {
    position: relative;
    width: 1008px;
    height: 1200px;
  }
  .card {
    position: absolute;
    left: 52px;
    width: 904px;
    background: var(--paper);
    overflow: hidden;
  }
  .card--front { top: 41px; height: 537px; }
  .card--back  { top: 621px; height: 536px; }

  .front-panel {
    position: absolute;
    left: 0; top: 0;
    width: 223px; height: 100%;
    background: var(--lime);
  }
  .front-title,
  .front-name {
    position: absolute;
    top: 142px;
    font-size: 50px;
    line-height: 50px;
    white-space: nowrap;
  }
  .front-title { left: 64px; color: var(--paper); }
  .front-name  { left: 229px; color: var(--lime); }

  .back-name {
    position: absolute;
    left: 0; top: 87px;
    padding-left: 69px;
    padding-bottom: 3px;
    font-size: 42px;
    line-height: 42px;
    color: var(--ink);
    border-bottom: 3px solid var(--lime);
    white-space: nowrap;
  }
  .back-online {
    position: absolute;
    left: 69px; top: 244px;
    font-size: 30px;
    line-height: 64px;
    color: var(--lime);
  }
  .back-online p { height: 64px; line-height: 30px; }
  .back-band {
    position: absolute;
    left: 0; top: 356px;
    width: 100%; height: 180px;
    background: var(--lime);
  }
  .back-phones {
    position: absolute;
    left: 69px; top: 20px;
    font-size: 32px;
    line-height: 51px;
    color: var(--paper);
  }
</style>
</head>
<body>
<main class="canvas">
  <section class="card card--front">
    <div class="front-panel"></div>
    <span class="front-title">Pastor</span>
    <span class="front-name">Neil R. Whitcombe</span>
  </section>

  <section class="card card--back">
    <h1 class="back-name" style="font-weight:400">Pastor Neil R. Whitcombe</h1>
    <div class="back-online">
      <p>www.harborptfell.example</p>
      <p>e-mail: pastor@harborptfell.example</p>
    </div>
    <div class="back-band">
      <div class="back-phones">
        <p>Phone: 555-318-2640</p>
        <p>Fax: 555-482-9157</p>
      </div>
    </div>
  </section>
</main>
</body>
</html>
```